Velvette by Monica Darsh business cards

I am after a business card that will fit the name of my business - velvette.
I want something classy and sexy and nothing tacky.
Ideas that I like are Zebra print backgrounds glitter back grounds
Two ideas I had were
1. Zebra print in black and white, the name Velvette by Monica Darsh and a shilouette of a woman laying on top of the name. Or instead of zebra a glitter background.
2. Idea very similar except for instead of a woman a pair of lips maybe a hot pink glitter or a gold glitter depending on background with the business name between the lips.
Or you can do something completely different.

Industry/Entity Type

Business

```html
<!DOCTYPE html>
<html lang="en">
<head>
<meta charset="utf-8">
<title>Velvette by Monica Darsh — Business Cards</title>
<link href="https://fonts.googleapis.com/css2?family=Open+Sans:wght@400;700&display=swap" rel="stylesheet">
<style>
  :root {
    --page-bg: #e9e6e2;
    --card-white: #ffffff;
    --card-black: #0b0b0b;
    --zebra-dark: #2b2b2b;
    --zebra-mid: #6b6b6b;
    --accent-pink: #f07272;
    --ink: #3a3a3a;
    --text-light: #f5f5f5;
    --mark-grey: #4a4a4a;
  }
  * { margin: 0; padding: 0; box-sizing: border-box; }
  html, body {
    width: 1200px; height: 900px; overflow: hidden;
    background: var(--page-bg);
    font-family: "Open Sans", Arial, sans-serif;
  }
  .canvas { position: relative; width: 1200px; height: 900px; }
  .card {
    position: absolute; left: 280px; width: 640px; height: 366px;
    overflow: hidden;
    box-shadow: 0 10px 28px rgba(0,0,0,0.25);
  }
  .card-front { top: 52px; background: var(--card-white); }
  .card-back { top: 482px; background: var(--card-black); }

  .zebra-band {
    position: absolute; left: 0; width: 100%;
    background: linear-gradient(160deg, var(--zebra-dark) 0%, var(--zebra-mid) 50%, var(--zebra-dark) 100%);
  }
  .zebra-top { top: 0; height: 104px; }
  .zebra-bottom { bottom: 0; height: 140px; }

  .logo-band {
    position: absolute; left: 0; top: 104px; width: 100%; height: 122px;
    display: flex; align-items: center; justify-content: center; gap: 18px;
  }
  .brand-mark {
    width: 40px; height: 40px; background: var(--accent-pink); flex: none;
  }
  .brand-text { display: flex; flex-direction: column; align-items: center; }
  .brand-name {
    font-weight: 400; font-size: 48px; color: var(--ink);
    letter-spacing: 1px; line-height: 1.05;
  }
  .brand-byline {
    font-weight: 400; font-size: 15px; color: var(--ink); margin-top: 4px;
  }

  .back-brand {
    position: absolute; left: 70px; top: 214px;
    display: flex; align-items: center; gap: 16px;
  }
  .back-mark { width: 36px; height: 36px; background: var(--mark-grey); flex: none; }
  .back-name {
    font-weight: 400; font-size: 60px; color: var(--text-light); line-height: 1;
  }
  .contact {
    position: absolute; left: 400px; top: 60px;
    color: var(--text-light); font-size: 15px; line-height: 1.4;
  }
  .contact-name { font-weight: 700; font-size: 19px; letter-spacing: 1px; margin-bottom: 4px; }
  .contact-line { font-weight: 400; }
</style>
</head>
<body>
<main class="canvas">
  <section class="card card-front">
    <div class="zebra-band zebra-top" role="img" aria-label="Black and white zebra print pattern"></div>
    <div class="logo-band">
      <div class="brand-mark"></div>
      <div class="brand-text">
        <div class="brand-name">Velvette</div>
        <div class="brand-byline">by Monica Darsh</div>
      </div>
    </div>
    <div class="zebra-band zebra-bottom" role="img" aria-label="Black and white zebra print pattern"></div>
  </section>

  <section class="card card-back">
    <div class="contact">
      <div class="contact-name">MONICA DARSH</div>
      <div class="contact-line">+123 456 7890</div>
      <div class="contact-line">monica@mail.com</div>
      <div class="contact-line">Address</div>
      <div class="contact-line">website</div>
    </div>
    <div class="back-brand">
      <div class="back-mark"></div>
      <div class="back-name">Velvette</div>
    </div>
  </section>
</main>
</body>
</html>
```